Brindlecove.io - Please redesign to make it look better from current design

We already have the current website, that you can access but we think it can improve from current version.
Brindlecove is a cryptocurrency hedge fund that allow you to participate in the hedge fund with cryptocurrency such as eth.
At current phase, we are doing an ICO, then we want to make sure that the website it looks professional, beautiful and trustable enough for investors after looking at our website.
Target Market(s)
Investors
Industry/Entity Type
Investment
Coding
Coded - Design and coding required
Number of Pages Required
1 page
Look and feel

```html
<!DOCTYPE html>
<html lang="en">
<head>
<meta charset="utf-8">
<title>Brindlecove — Digital Asset Management</title>
<link href="https://fonts.googleapis.com/css2?family=Roboto:wght@300;400;500;700&family=Roboto+Condensed:wght@400;700&display=swap" rel="stylesheet">
<style>
:root{
  --navy:#0c2b6b;
  --navy-deep:#0a2259;
  --sky:#1f8fe3;
  --ink:#222831;
  --muted:#555b66;
  --line:#dcdfe4;
  --dark:#2b2d31;
  --footer:#26282c;
  --white:#ffffff;
}
*{box-sizing:border-box;margin:0;padding:0}
html,body{width:1200px;height:3579px;overflow:hidden}
body{position:relative;background:var(--white);font-family:"Roboto",sans-serif;color:var(--ink)}
.abs{position:absolute}

/* header */
.hero{left:0;top:0;width:1200px;height:573px;background:linear-gradient(120deg,#cfc7bd 0%,#b9ada0 35%,#8f8579 65%,#b7b3ae 100%)}
.topbar{left:0;top:0;width:1200px;height:92px;background:rgba(255,255,255,.88)}
.brand{left:167px;top:26px;display:flex;align-items:center;gap:12px;font:700 28px "Roboto",sans-serif;color:var(--navy)}
.brand i{width:30px;height:30px;border-radius:50%;background:var(--navy);display:block}
.nav{left:649px;top:36px;display:flex;gap:40px;font:500 14px "Roboto",sans-serif;color:var(--ink);letter-spacing:.3px}
.nav .on{color:var(--navy)}
.hero-title{left:0;top:318px;width:1184px;text-align:center;font-family:"Roboto Condensed",sans-serif;font-weight:700;line-height:1}
.hero-title .a{display:block;font-size:50px;color:var(--navy)}
.hero-title .b{display:block;font-size:36px;color:var(--white);margin-top:6px;font-weight:400}

/* services */
.eyebrow{left:0;top:624px;width:1200px;text-align:center;font:500 13px "Roboto",sans-serif;letter-spacing:.5px}
.h2{left:0;width:1200px;text-align:center;font:700 30px "Roboto Condensed",sans-serif;color:var(--navy)}
.lead{left:205px;top:694px;width:790px;text-align:center;font:400 11px/18px "Roboto",sans-serif;color:var(--muted)}
.card{top:766px;width:272px;height:301px;border:1px solid var(--line);text-align:center}
.card .ic{display:block;margin:36px auto 0;width:86px;height:86px}
.card h3{margin-top:20px;font:400 16px/1 "Roboto Condensed",sans-serif;color:var(--navy)}
.card h3 b{display:block;font-weight:700;font-size:19px;margin-top:2px}
.card p{margin:16px auto 0;width:212px;font:400 11px/16px "Roboto",sans-serif;color:var(--muted)}

/* about */
.about-band{left:0;top:1133px;width:508px;height:525px;background:linear-gradient(135deg,#12306f,#0b2460)}
.frame{background:var(--white);padding:16px;box-shadow:0 4px 18px rgba(0,0,0,.18)}
.about-frame{left:172px;top:1186px;width:382px;height:417px}
.ph{width:100%;height:100%}
.about-title{left:625px;top:1196px;font:700 40px/46px "Roboto Condensed",sans-serif;color:var(--navy)}
.about-sub{left:625px;top:1241px;font:400 18px/22px "Roboto",sans-serif;color:var(--ink)}
.about-copy{left:625px;top:1272px;width:352px;font:400 9px/14.5px "Roboto",sans-serif;color:var(--muted);text-align:justify}
.about-copy p+p{margin-top:8px}
.btn-out{left:627px;top:1551px;width:113px;height:34px;border:2px solid var(--navy);font:700 11px/30px "Roboto",sans-serif;color:var(--navy);text-align:center}

/* banner */
.banner{left:0;top:1718px;width:1200px;height:246px;background:linear-gradient(100deg,#3a3c40,#24262a 55%,#35373b)}
.banner h2{position:absolute;left:0;top:62px;width:1200px;text-align:center;font:700 30px/34px "Roboto Condensed",sans-serif;color:var(--white)}
.btn-sky{left:503px;top:1878px;width:206px;height:36px;background:var(--sky);color:var(--white);font:700 13px/36px "Roboto Condensed",sans-serif;text-align:center}

/* process */
.proc-band{left:699px;top:2023px;width:501px;height:525px;background:linear-gradient(135deg,#12306f,#0b2460)}
.proc-frame{left:661px;top:2083px;width:384px;height:410px}
.proc-title{left:167px;top:2094px;font:700 36px "Roboto Condensed",sans-serif;color:var(--navy)}
.proc-h{left:167px;font:700 16px "Roboto",sans-serif;color:var(--ink)}
.proc-copy{left:167px;top:2184px;width:453px;font:400 11px/18px "Roboto",sans-serif;color:var(--muted)}
.proc-list{left:167px;top:2320px;font:400 11px/24px "Roboto",sans-serif;color:var(--muted);list-style:none}

/* team */
.rule{left:575px;top:2643px;width:50px;height:3px;background:var(--navy)}
.member{top:2701px;width:279px;height:394px;border:1px solid var(--line);border-bottom:6px solid var(--navy);text-align:center}
.member.hl{background:var(--navy);border-color:var(--navy)}
.member .ph{display:block;width:205px;height:172px;margin:25px auto 0}
.member h4{margin-top:20px;font:700 15px "Roboto",sans-serif;color:var(--ink)}
.member .role{margin-top:4px;font:400 14px "Roboto",sans-serif;color:var(--ink)}
.member p{margin:8px auto 0;width:220px;font:400 11px/15px "Roboto",sans-serif;color:var(--muted)}
.member.hl h4,.member.hl .role,.member.hl p{color:var(--white)}
.socials{display:flex;justify-content:center;gap:14px}
.member .socials{position:absolute;left:0;right:0;top:340px}
.dot{width:30px;height:30px;border-radius:50%;border:1.5px solid var(--ink)}
.member.hl .dot{border-color:var(--white)}

/* footer */
.footer{left:0;top:3161px;width:1200px;height:382px;background:var(--footer)}
.email{left:363px;top:3214px;width:334px;height:36px;background:var(--white);font:400 11px/36px "Roboto",sans-serif;color:#8a8f98;padding-left:14px}
.subscribe{left:697px;top:3214px;width:107px;height:36px;background:var(--navy);color:var(--white);font:700 12px/36px "Roboto",sans-serif;text-align:center}
.f-brand{left:0;top:3290px;width:1200px;display:flex;justify-content:center;align-items:center;gap:10px;font:700 26px "Roboto",sans-serif;color:var(--white)}
.f-brand i{width:26px;height:26px;border-radius:50%;background:var(--white);display:block}
.f-copy{left:330px;top:3366px;width:540px;text-align:center;font:400 11px/17px "Roboto",sans-serif;color:#8d9199}
.f-social{left:0;top:3436px;width:1200px;gap:12px}
.f-social .dot{width:24px;height:24px;border-color:#cfd2d7}
.f-contact{left:0;top:3484px;width:1200px;display:flex;justify-content:center;gap:60px;font:400 11px "Roboto",sans-serif;color:#b3b7be}
.f-contact span{display:flex;align-items:center;gap:6px}
.bottom{left:0;top:3543px;width:1200px;height:36px;background:var(--navy-deep);text-align:center;font:400 11px/36px "Roboto",sans-serif;color:#c9d1e6}
</style>
</head>
<body>

<header>
  <div class="abs hero" role="img" aria-label="Photo of three business colleagues reviewing a tablet together on a sofa"></div>
  <div class="abs topbar"></div>
  <div class="abs brand"><i></i>Brindlecove</div>
  <nav class="abs nav"><span class="on">HOME</span><span>ABOUT</span><span>SERVICES</span><span>PROJECTS</span><span>CONTACT</span></nav>
  <h1 class="abs hero-title"><span class="a">BRINDLECOVE</span><span class="b">DIGITAL ASSET MANAGEMENT</span></h1>
</header>

<section class="services">
  <div class="abs eyebrow">OUR SERVICES</div>
  <h2 class="abs h2" style="top:642px">WHAT WE OFFER</h2>
  <p class="abs lead">Lorem Ipsum is simply dummy text of the printing and typesetting industry. Lorem Ipsum has been the industry's standard dummy text ever since the 1500s. It has survived not only five centuries, but also the leap into electronic typesetting, remaining essentially unchanged. It was popularised with software like Quillset Composer including versions of Lorem Ipsum.</p>

  <div class="abs card" style="left:167px">
    <svg class="ic" viewBox="0 0 86 86"><circle cx="43" cy="43" r="43" fill="#0c2b6b"/><rect x="26" y="48" width="7" height="12" fill="#fff"/><rect x="37" y="42" width="7" height="18" fill="#fff"/><rect x="48" y="36" width="7" height="24" fill="#fff"/><path d="M24 42 L38 30 L46 36 L60 24" stroke="#fff" stroke-width="3" fill="none"/><path d="M54 24 H60 V30" stroke="#fff" stroke-width="3" fill="none"/></svg>
    <h3>MARKET<b>FORECASTING</b></h3>
    <p>Lorem Ipsum is simply dummy text of the printing and typesetting industry. Lorem Ipsum has been the industry's standard dummy text took a galley of type and scrambled it to make type specimen book.</p>
  </div>
  <div class="abs card" style="left:470px">
    <svg class="ic" viewBox="0 0 86 86"><circle cx="43" cy="43" r="43" fill="#0c2b6b"/><rect x="29" y="22" width="28" height="42" rx="3" fill="#fff"/><rect x="33" y="27" width="20" height="8" fill="#0c2b6b"/><g fill="#0c2b6b"><rect x="33" y="39" width="5" height="5"/><rect x="41" y="39" width="5" height="5"/><rect x="49" y="39" width="4" height="5"/><rect x="33" y="47" width="5" height="5"/><rect x="41" y="47" width="5" height="5"/><rect x="49" y="47" width="4" height="5"/><rect x="33" y="55" width="5" height="5"/><rect x="41" y="55" width="5" height="5"/><rect x="49" y="55" width="4" height="5"/></g></svg>
    <h3>FINANCIAL<b>PLANNING</b></h3>
    <p>Lorem Ipsum is simply dummy text of the printing and typesetting industry. Lorem Ipsum has been the industry's standard dummy text took a galley of type and scrambled it to make type specimen book.</p>
  </div>
  <div class="abs card" style="left:773px">
    <svg class="ic" viewBox="0 0 86 86"><circle cx="43" cy="43" r="43" fill="#0c2b6b"/><rect x="27" y="22" width="26" height="38" rx="2" fill="none" stroke="#fff" stroke-width="3"/><rect x="32" y="44" width="4" height="10" fill="#fff"/><rect x="38" y="38" width="4" height="16" fill="#fff"/><rect x="44" y="32" width="4" height="22" fill="#fff"/><circle cx="54" cy="56" r="7" fill="none" stroke="#fff" stroke-width="3"/><path d="M59 61 L65 67" stroke="#fff" stroke-width="3"/></svg>
    <h3>FINANCIAL<b>ANALYSIS</b></h3>
    <p>Lorem Ipsum is simply dummy text of the printing and typesetting industry. Lorem Ipsum has been the industry's standard dummy text took a galley of type and scrambled it to make type specimen book.</p>
  </div>
</section>

<section class="about">
  <div class="abs about-band" role="img" aria-label="Dark blue tinted background photo of a business crowd with finance words"></div>
  <div class="abs frame about-frame"><div class="ph" role="img" aria-label="Photo of three colleagues smiling over a blue folder" style="background:linear-gradient(135deg,#d9c9b3,#b89a7c 50%,#8e7b6a)"></div></div>
  <h2 class="abs about-title">BRINDLECOVE</h2>
  <div class="abs about-sub">Digital Asset Management</div>
  <div class="abs about-copy">
    <p>Brindlecove process and manages on hedge fund strategy models which invests in a diversified portfolio of blockchain tokens. Blockchain tokens are emerging which add a monetary incentive layer to p2p protocols and facilitate equity crowdfunding that anyone in the world can participate in. This means open source software developers can monetize their networks at the protocol level and users of the network are the equity owners of the network. For this conditions, returns will go to holders of the tokens.</p>
    <p>However, because of Cryptocurrency having almost 1,000 currencies and digital assets combine. The price is high volatility and high for speculation or investing. Therefore, Brindlecove manages on hedge fund strategy models which speculate and invest in a diversified portfolio of blockchain tokens. The objective on this strategy model is preserve capital, mitigate risk and generate absolute returns mainly by trading Cryptocurrency Markets. Brindlecove is employing a market neutral, long/short equity strategy. Our system manages a diverse portfolio and uses our proprietary research, modeling, risk management, and execution technology to identify and capitalize on size-constrained market opportunities.</p>
  </div>
  <div class="abs btn-out">READ MORE &#x276F;</div>
</section>

<section class="abs banner" role="img" aria-label="Dark photo of a laptop keyboard">
  <h2>WE SPECILIZE IN INVESTING WITH TECHNOLOGY STARTUPS<br>IN THE BAY AREA</h2>
</section>
<div class="abs btn-sky">DOWNLOAD WHITEPAPER</div>

<section class="process">
  <div class="abs proc-band"></div>
  <div class="abs frame proc-frame"><div class="ph" role="img" aria-label="Photo of a hand pointing at charts on a tablet" style="background:linear-gradient(135deg,#c9ced6,#8e97a6 50%,#4d5565)"></div></div>
  <h2 class="abs proc-title">PROCESS</h2>
  <h3 class="abs proc-h" style="top:2148px">Hedge Fund Model</h3>
  <p class="abs proc-copy">Brindlecove run on closed-end fund (CEF) model which offers its shares to investors and utilize the fund to speculate and invest in the innovative blockchain tokens. Brindlecove will charge an upfront annual operation fee 4% of the money raised during the ICO. After that, the fund will charge a quarterly performance of 50% on the net profit made.</p>
  <h3 class="abs proc-h" style="top:2280px">Net Profit Distribution</h3>
  <ul class="abs proc-list">
    <li>50 % of net profit is distributed to investors</li>
    <li>0 – 5 % net profit = 0% performance fee</li>
    <li>6 – 10% net profit = 5% performance fee</li>
    <li>10-15 % net profit = 10% performance fee</li>
    <li>&gt;15% net profit &gt; 15% performance fee</li>
    <li>The remainder&nbsp; (50% minus performance fee, so at least 35%) is reinvested</li>
  </ul>
</section>

<section class="team">
  <h2 class="abs h2" style="top:2594px;font-size:34px">EXECUTIVE TEAM</h2>
  <div class="abs rule"></div>

  <div class="abs member" style="left:167px">
    <div class="ph" role="img" aria-label="Portrait photo of the director" style="background:linear-gradient(180deg,#6b5a4d,#3e3833)"></div>
    <h4>Daniel Vantreese</h4><div class="role">Director</div>
    <p>As a hedge fund manager, Vantreese is the Chief Executive Officer of Fenwick Ridge Capital LLC, an investment manager of Copperline Growth Fund SP</p>
    <div class="socials"><span class="dot"></span><span class="dot"></span><span class="dot"></span></div>
  </div>
  <div class="abs member hl" style="left:465px">
    <div class="ph" role="img" aria-label="Portrait photo of the technical advisor" style="background:linear-gradient(180deg,#c7d4dc,#8fa3b0)"></div>
    <h4>Marcus Okonedo</h4><div class="role">Technical advisor</div>
    <p>Okonedo has various experienced on cryptocurrency and blockchain technology. He created what was the world's 4th most valuable cryptocurrency in February 2014.</p>
    <div class="socials"><span class="dot"></span><span class="dot"></span><span class="dot"></span></div>
  </div>
  <div class="abs member" style="left:764px">
    <div class="ph" role="img" aria-label="Portrait photo of the marketing consultant" style="background:linear-gradient(180deg,#9b4a32,#5d2a1e)"></div>
    <h4>Julian Harrowgate</h4><div class="role">Marketing Consultant</div>
    <p>Harrowgate embeds a decade of experience in brand building, strategic planning, and marketing communication across the global agencies.</p>
    <div class="socials"><span class="dot"></span><span class="dot"></span><span class="dot"></span></div>
  </div>
</section>

<footer>
  <div class="abs footer" role="img" aria-label="Dark background photo of a business crowd"></div>
  <div class="abs email">Enter Your Email Id</div>
  <div class="abs subscribe">SUBSCRIBE</div>
  <div class="abs f-brand"><i></i>Brindlecove</div>
  <p class="abs f-copy">Sed et libero nec sem lacinia dapibus nec vel felis. Vivamus fringilla magna et eros laoreet commodo venenatis et lectus. Sed vitae dui in elit tincidunt pretium. Nam vel blandit neque, aenean ultrices a lorem vitae mollis.</p>
  <div class="abs socials f-social"><span class="dot"></span><span class="dot"></span><span class="dot"></span></div>
  <div class="abs f-contact">
    <span><svg width="10" height="13" viewBox="0 0 10 13"><path d="M5 0a5 5 0 0 0-5 5c0 4 5 8 5 8s5-4 5-8a5 5 0 0 0-5-5zm0 7a2 2 0 1 1 0-4 2 2 0 0 1 0 4z" fill="#b3b7be"/></svg>14 Larkspur Lane, Eastmoor, London.</span>
    <span><svg width="13" height="10" viewBox="0 0 13 10"><rect x=".5" y=".5" width="12" height="9" fill="none" stroke="#b3b7be"/><path d="M.5 .5 L6.5 5.5 L12.5 .5" fill="none" stroke="#b3b7be"/></svg>info@brindlecove.io</span>
    <span><svg width="11" height="11" viewBox="0 0 11 11"><path d="M2 0l2 2.5-1 1.5c.8 1.6 1.9 2.7 3.5 3.5l1.5-1L10.5 8.5 9 11C4 10.5.5 7 0 2z" fill="#b3b7be"/></svg>+44 20 7946 0321</span>
  </div>
  <div class="abs bottom">© 2017 BRINDLECOVE. All rights reserved</div>
</footer>

</body>
</html>
```